Unique, Impressive, and Modern Business Card

Looking for a distinctive, unique business card. We are distributors of tire repairs supplies, tools, machinery, and chemicals. Our target market are tire repair shops, tire franchises, and mechanic shops. We would like our design to include tire characteristics, and use our business colors. Feel free to use all types design and printing options (emboss, spot uv, foil, etc) QR code may be applied, you can use different size business cards ( standard, square, rounded edge, colored edge, etc), all formats needed for printing, also editable for future changes

Target Market(s)

Automotive, Tire industries

Industry/Entity Type

Tire Industry (automotive)

Contact Information for Business Card

Business logo, business Name (Corvane Supply Inc), Name (Marcus Pellow), Position (President) Address (58 Fernhollow Lane, Alder Ridge OR 97742), Contact number (Company 1-855-302-4418, Cell 1-541-245-9073, email address (marcus.pellow@corvanesupply.com), URL (www.corvanesupply.com

Requirements
Must have
• Must include Business Colors (Black, Green, Blue, White) see sample website file
Nice to have
• emboss, spot uv, etc

```html
<!DOCTYPE html>
<html lang="en">
<head>
<meta charset="utf-8">
<title>Corvane Supply Inc – Business Card</title>
<link rel="stylesheet" href="https://fonts.googleapis.com/css2?family=Montserrat:wght@400;500;700&display=swap">
<style>
  :root {
    --canvas-bg: #d9d9db;
    --card-white: #ffffff;
    --card-black: #1b1b1c;
    --ink: #161616;
    --ink-soft: #4a4a4a;
    --brand-blue: #2b48a8;
    --pattern-light: #7a7a7a;
    --pattern-dark: #2a2a2b;
  }
  * { box-sizing: border-box; margin: 0; padding: 0; }
  html, body { width: 1200px; height: 1200px; overflow: hidden; }
  body {
    background: var(--canvas-bg);
    font-family: "Montserrat", sans-serif;
    position: relative;
  }
  .card {
    position: absolute;
    top: 232px;
    width: 420px;
    height: 735px;
    border-radius: 30px;
    overflow: hidden;
    box-shadow: 0 10px 30px rgba(0,0,0,0.18);
  }
  .card--front { left: 150px; background: var(--card-white); text-align: center; color: var(--ink); }
  .card--back { left: 630px; background: var(--card-black); }

  .brand { position: absolute; left: 0; right: 0; display: flex; flex-direction: column; align-items: center; }
  .brand__mark { width: 62px; height: 62px; border-radius: 50%; }
  .brand__name {
    margin-top: 14px;
    font-weight: 500;
    font-size: 40px;
    letter-spacing: -0.5px;
    line-height: 1;
    text-transform: uppercase;
    white-space: nowrap;
  }
  .card--front .brand { top: 58px; }
  .card--front .brand__mark { background: var(--ink); }
  .card--front .brand__name { color: var(--ink); }

  .person { position: absolute; top: 232px; left: 0; right: 0; }
  .person__name { color: var(--brand-blue); font-weight: 700; font-size: 27px; }
  .person__title { color: var(--ink-soft); font-size: 17px; margin-top: 2px; }

  .icon-row {
    position: absolute; top: 318px; left: 50px; right: 50px;
    display: flex; align-items: center; gap: 8px;
  }
  .icon-row__rule { flex: 1; height: 2px; background: var(--brand-blue); }
  .icon {
    width: 28px; height: 28px; border-radius: 4px;
    background: var(--brand-blue);
    display: flex; align-items: center; justify-content: center;
  }
  .icon svg { width: 18px; height: 18px; }

  .contact { position: absolute; top: 376px; left: 0; right: 0; font-size: 16.5px; line-height: 1.5; color: var(--ink); }
  .divider { position: absolute; top: 560px; left: 160px; width: 100px; height: 2px; background: var(--brand-blue); }
  .address { position: absolute; top: 594px; left: 0; right: 0; font-size: 15px; line-height: 1.45; color: var(--ink-soft); }

  .symbol-grid {
    position: absolute; top: 0; left: 0; right: 0; height: 520px;
    background: linear-gradient(200deg, var(--pattern-light) 0%, #4a4a4b 45%, var(--pattern-dark) 100%);
    -webkit-mask-image: linear-gradient(180deg, #000 55%, transparent 100%);
            mask-image: linear-gradient(180deg, #000 55%, transparent 100%);
    opacity: 0.85;
  }
  .card--back .brand { top: 520px; }
  .card--back .brand__mark { background: var(--card-white); }
  .card--back .brand__name { color: var(--card-white); }
</style>
</head>
<body>

  <section class="card card--front" aria-label="Business card front">
    <div class="brand">
      <div class="brand__mark"></div>
      <div class="brand__name">Corvane Supply</div>
    </div>

    <div class="person">
      <div class="person__name">Marcus Pellow</div>
      <div class="person__title">President</div>
    </div>

    <div class="icon-row">
      <span class="icon-row__rule"></span>
      <span class="icon" aria-label="Phone">
        <svg viewBox="0 0 24 24"><path fill="#fff" d="M6.6 10.8a15 15 0 0 0 6.6 6.6l2.2-2.2a1 1 0 0 1 1-.25 11.4 11.4 0 0 0 3.6.57 1 1 0 0 1 1 1V20a1 1 0 0 1-1 1A17 17 0 0 1 3 4a1 1 0 0 1 1-1h3.5a1 1 0 0 1 1 1c0 1.250.2 2.46.57 3.6a1 1 0 0 1-.25 1z"/></svg>
      </span>
      <span class="icon" aria-label="Mobile">
        <svg viewBox="0 0 24 24"><rect x="7" y="2.5" width="10" height="19" rx="2" fill="none" stroke="#fff" stroke-width="2"/><circle cx="12" cy="18" r="1.2" fill="#fff"/></svg>
      </span>
      <span class="icon" aria-label="Email">
        <svg viewBox="0 0 24 24"><rect x="3" y="5.5" width="18" height="13" rx="1.5" fill="#fff"/><path d="M3.5 6.5 12 13l8.5-6.5" fill="none" stroke="#2b48a8" stroke-width="1.6"/></svg>
      </span>
      <span class="icon" aria-label="Website">
        <svg viewBox="0 0 24 24"><circle cx="12" cy="12" r="8.5" fill="none" stroke="#fff" stroke-width="1.8"/><path d="M3.5 12h17M12 3.5c3 3 3 14 0 17M12 3.5c-3 3-3 14 0 17" fill="none" stroke="#fff" stroke-width="1.4"/></svg>
      </span>
      <span class="icon-row__rule"></span>
    </div>

    <div class="contact">
      <div>1-855-302-4418</div>
      <div>1-541-245-9073</div>
      <div>marcus.pellow@corvanesupply.com</div>
      <div>www.corvanesupply.com</div>
    </div>

    <div class="divider"></div>

    <div class="address">
      <div>58 Fernhollow Lane</div>
      <div>Alder Ridge OR 97742</div>
    </div>
  </section>

  <section class="card card--back" aria-label="Business card back">
    <div class="symbol-grid" role="img" aria-label="Repeating grid of the company symbol fading from light grey to black, spot UV pattern"></div>
    <div class="brand">
      <div class="brand__mark"></div>
      <div class="brand__name">Corvane Supply</div>
    </div>
  </section>

</body>
</html>
```